riverstonelightcare - healing business promotion

I have and energy / intuitive healing and kinesiology business. working with people who are looking for healing outside of the modern medical model, who have tried but failed in their search for understanding their conditions and why health and or happiness eludes them. the healing is done with love, patience and understanding. I am looking to be taken seriously with my presentation and to reach a person who may be deterred by the thought of angels and intuition! but to not exclude those that are attracted to that also.

Industry/Entity Type

Medical

Contact Information for Business Card

riverstonelightcare
calm clear gentle energy renewal method
tamsin corrine hale
energy healing / kinesiology and neurotraining
0417362815 07 4186 2751
home visits available for cairns and tablelands
t.chale@maildrop-example.net

Requirements
Should not have
• Primary colours

```html
<!DOCTYPE html>
<html lang="en">
<head>
<meta charset="utf-8">
<title>Riverstonelightcare – Business Card</title>
<link rel="stylesheet" href="https://fonts.googleapis.com/css2?family=Cinzel:wght@400&family=Questrial&family=Open+Sans:ital,wght@0,700;1,700&display=swap">
<style>
  :root {
    --lilac: #a67cf6;
    --lilac-light: #c3a3fb;
    --violet-deep: #5118f2;
    --violet-band: #7b4cf6;
    --violet-text: #5a22e6;
    --glow: rgba(255, 240, 255, 0.55);
    --white: #ffffff;
  }
  html, body {
    margin: 0;
    padding: 0;
    width: 1200px;
    height: 741px;
    overflow: hidden;
    background: var(--lilac);
  }
  .card {
    position: relative;
    width: 1200px;
    height: 741px;
    overflow: hidden;
    background:
      radial-gradient(circle at 40px 230px, var(--glow) 0, rgba(255,255,255,0) 70px),
      radial-gradient(circle at 400px 520px, rgba(255,220,255,0.5) 0, rgba(255,255,255,0) 90px),
      radial-gradient(circle at 290px 600px, rgba(255,235,255,0.35) 0, rgba(255,255,255,0) 80px),
      radial-gradient(circle at 760px 245px, rgba(255,255,255,0.22) 0, rgba(255,255,255,0) 50px),
      radial-gradient(circle at 630px 330px, rgba(255,255,255,0.18) 0, rgba(255,255,255,0) 45px),
      radial-gradient(circle at 130px 700px, rgba(255,230,255,0.4) 0, rgba(255,255,255,0) 90px),
      linear-gradient(90deg,
        rgba(255,255,255,0) 0, rgba(255,255,255,0.25) 30px, rgba(255,255,255,0) 80px,
        rgba(255,255,255,0) 190px, rgba(255,255,255,0.2) 215px, rgba(255,255,255,0) 240px,
        rgba(255,255,255,0) 330px, rgba(255,255,255,0.25) 350px, rgba(255,255,255,0) 420px,
        rgba(255,255,255,0) 100%),
      linear-gradient(180deg, var(--lilac-light) 0%, var(--lilac) 45%, #a075f5 100%);
  }
  .brand {
    position: absolute;
    left: 56px;
    top: 96px;
    display: flex;
    align-items: center;
    gap: 22px;
  }
  .brand-dot {
    width: 54px;
    height: 54px;
    border-radius: 50%;
    background: var(--violet-deep);
  }
  .brand-name {
    font-family: "Questrial", sans-serif;
    font-size: 58px;
    color: var(--white);
    line-height: 1;
    letter-spacing: 0.5px;
  }
  .tagline-band {
    position: absolute;
    left: 211px;
    top: 168px;
    width: 989px;
    height: 38px;
    background: linear-gradient(90deg, rgba(123,76,246,0.55) 0%, var(--violet-band) 60%, #8656f7 100%);
  }
  .tagline {
    position: absolute;
    left: 224px;
    top: 170px;
    font-family: "Cinzel", serif;
    font-size: 29px;
    color: var(--white);
    letter-spacing: 1.6px;
    line-height: 34px;
    white-space: nowrap;
  }
  .contact-panel {
    position: absolute;
    left: 516px;
    top: 365px;
    width: 684px;
    height: 246px;
    border-radius: 34px 0 0 34px;
    background: var(--white);
    overflow: hidden;
  }
  .contact-panel-fill {
    height: 199px;
    background: var(--violet-deep);
  }
  .person-name {
    position: absolute;
    left: 544px;
    top: 377px;
    font-family: "Questrial", sans-serif;
    font-size: 42px;
    color: var(--white);
    letter-spacing: 1px;
    white-space: nowrap;
  }
  .person-role {
    position: absolute;
    left: 546px;
    top: 430px;
    font-family: "Questrial", sans-serif;
    font-size: 27px;
    color: var(--white);
    white-space: nowrap;
  }
  .contact-line {
    position: absolute;
    left: 548px;
    display: flex;
    align-items: center;
    gap: 12px;
    color: var(--white);
    white-space: nowrap;
  }
  .contact-phone {
    top: 474px;
    font-family: "Open Sans", sans-serif;
    font-weight: 700;
    font-size: 30px;
  }
  .contact-email {
    top: 522px;
    font-family: "Questrial", sans-serif;
    font-size: 28px;
  }
  .home-visits {
    position: absolute;
    left: 548px;
    top: 574px;
    font-family: "Open Sans", sans-serif;
    font-weight: 700;
    font-style: italic;
    font-size: 22px;
    color: var(--violet-text);
    white-space: nowrap;
  }
</style>
</head>
<body>
  <main class="card">
    <div class="brand">
      <div class="brand-dot"></div>
      <div class="brand-name">riverstonelightcare</div>
    </div>

    <div class="tagline-band"></div>
    <div class="tagline">CALM CLEAR GENTLE ENERGY RENEWAL METHOD</div>

    <div class="contact-panel"><div class="contact-panel-fill"></div></div>

    <div class="person-name">Tamsin Corrine Hale</div>
    <div class="person-role">Energy Healing / Kinesiology &amp; Neurotraining</div>

    <div class="contact-line contact-phone">
      <svg class="icon-phone" width="30" height="32" viewBox="0 0 30 32" aria-hidden="true">
        <rect x="0" y="0" width="30" height="32" rx="6" fill="#ffffff"/>
        <path d="M10 6 C8 7 7 9 7.5 12 C9 19 13 24 19 26.5 C21.5 27.5 23.5 26 24.5 24 L21 20.5 L18.5 22 C16 20.5 13.5 17 12.5 14 L14.5 12 L12 6 Z" fill="#5118f2"/>
      </svg>
      <span>0417362815 07 4186 2751</span>
    </div>

    <div class="contact-line contact-email">
      <svg class="icon-mail" width="30" height="22" viewBox="0 0 30 22" aria-hidden="true">
        <rect x="1.5" y="1.5" width="27" height="19" fill="none" stroke="#ffffff" stroke-width="2.2"/>
        <path d="M1.5 1.5 L15 12 L28.5 1.5 M1.5 20.5 L11 10 M28.5 20.5 L19 10" fill="none" stroke="#ffffff" stroke-width="2.2"/>
      </svg>
      <span>t.chale@maildrop-example.net</span>
    </div>

    <div class="home-visits">Home visits available for Cairns and Tablelands</div>
  </main>
</body>
</html>
```